Plakat-Design für Garten- und Landschaftsbau
Zielgruppe
Unsere Firma beschäftigt sich mit dem Garten- und Landschaftsbau, das heißt wie gestalten Gärten neu, führen Baggerarbeiten und Erdarbeiten durch.
Und sind in dem Forst und Rodungsarbeiten aktiv
Aufgabenstellung
Dies soll ein Banner sein das an Bauzäune angebracht wird Format bzw. Verhältnis sollte bxh 2:1 sein
Der Banner soll mit einen oder meheren Bildern versehen werden im Hintergrund oder im Vordergrund.

```html
<!DOCTYPE html>
<html lang="de">
<head>
<meta charset="utf-8">
<title>Gartenbau Brandauer – Bauzaunbanner</title>
<link rel="stylesheet" href="https://fonts.googleapis.com/css2?family=Delius&family=Roboto:wght@400;700&display=swap">
<style>
  :root {
    --hedge-dark: #1f3a22;
    --hedge-mid: #3d6234;
    --hedge-light: #6a8a4e;
    --panel-cream: #e9f2c4;
    --panel-dash: #8aa05a;
    --brand-green: #1f8a2e;
    --tick-light: #c9e84a;
    --tick-dark: #6aa321;
    --text-light: #ffffff;
    --box-dark: rgba(20, 40, 22, 0.78);
    --box-dash: #d8e86a;
  }
  * { margin: 0; padding: 0; box-sizing: border-box; }
  html, body { width: 1200px; height: 600px; overflow: hidden; background: #fff; }
  .banner { position: relative; width: 1200px; height: 600px; overflow: hidden; font-family: "Delius", cursive; }
  .banner-photo {
    position: absolute; inset: 0;
    background:
      radial-gradient(ellipse 220px 300px at 590px 300px, rgba(140,180,220,0.55), transparent 70%),
      radial-gradient(ellipse 500px 400px at 900px 120px, var(--hedge-light), transparent 70%),
      linear-gradient(180deg, var(--hedge-mid) 0%, var(--hedge-dark) 75%, #2b3a28 100%);
  }
  .brand-panel { position: absolute; left: 36px; top: 0; width: 428px; height: 290px; }
  .brand-panel svg { position: absolute; inset: 0; }
  .brand-name {
    position: absolute; left: 0; right: 0; top: 100px;
    display: flex; align-items: center; justify-content: center; gap: 12px;
    color: var(--brand-green); font-size: 30px; font-weight: 400;
  }
  .brand-dot { width: 22px; height: 22px; border-radius: 50%; background: var(--brand-green); }
  .service-list { position: absolute; left: 42px; top: 300px; list-style: none; }
  .service-list li, .feature-list li {
    display: flex; align-items: center; gap: 16px;
    color: var(--text-light); font-size: 36px; height: 53px;
    text-shadow: 0 2px 4px rgba(0,0,0,0.5);
  }
  .tick { width: 46px; height: 42px; flex: none; }
  .contact {
    position: absolute; right: 42px; top: 26px; text-align: right;
    font-family: "Roboto", sans-serif; color: var(--text-light);
    font-size: 22px; line-height: 36px; text-shadow: 0 1px 3px rgba(0,0,0,0.5);
  }
  .offer-box {
    position: absolute; left: 694px; top: 252px; width: 506px; height: 312px;
    background: var(--box-dark);
    border-top: 2px dashed var(--box-dash); border-left: 2px dashed var(--box-dash);
    padding: 24px 0 0 38px;
  }
  .offer-title { color: var(--text-light); font-size: 36px; font-weight: 400; line-height: 52px; margin-bottom: 30px; }
  .feature-list { list-style: none; margin-left: 4px; }
</style>
</head>
<body>
<main class="banner">
  <div class="banner-photo" role="img" aria-label="Foto: Frau im hellblauen Kleid mit grüner Gießkanne vor einer dichten grünen Hecke, daneben Schubkarren und Eimer"></div>

  <div class="brand-panel">
    <svg width="428" height="290" viewBox="0 0 428 290">
      <polygon points="0,0 428,0 428,205 214,290 0,205" fill="var(--panel-cream)"/>
      <polygon points="10,0 418,0 418,198 214,278 10,198" fill="none" stroke="var(--panel-dash)" stroke-width="2" stroke-dasharray="6 5"/>
      <line x1="50" y1="150" x2="378" y2="150" stroke="var(--brand-green)" stroke-width="3"/>
    </svg>
    <div class="brand-name"><span class="brand-dot"></span>Gartenbau Brandauer GmbH</div>
  </div>

  <svg width="0" height="0" style="position:absolute">
    <defs>
      <linearGradient id="tickFill" x1="0" y1="0" x2="0" y2="1">
        <stop offset="0" stop-color="var(--tick-light)"/>
        <stop offset="1" stop-color="var(--tick-dark)"/>
      </linearGradient>
      <symbol id="tick" viewBox="0 0 46 42">
        <path d="M3 22 L11 15 L19 25 L38 3 L44 9 L19 39 Z" fill="url(#tickFill)" stroke="#f4ffd0" stroke-width="1.5" stroke-linejoin="round"/>
      </symbol>
    </defs>
  </svg>

  <ul class="service-list">
    <li><svg class="tick"><use href="#tick"/></svg>Garten-und Landschaftsbau</li>
    <li><svg class="tick"><use href="#tick"/></svg>Baggerbetrieb</li>
    <li><svg class="tick"><use href="#tick"/></svg>Erdbau</li>
    <li><svg class="tick"><use href="#tick"/></svg>Gebäudemanagement</li>
    <li><svg class="tick"><use href="#tick"/></svg>Forst-und Rodungsarbeiten</li>
  </ul>

  <address class="contact" style="font-style:normal">
    0176/2894136<br>
    info@gartenbau-brandauer.de<br>
    www.gartenbau-brandauer.de
  </address>

  <section class="offer-box">
    <h2 class="offer-title">Individuelle<br>Gartengestaltung</h2>
    <ul class="feature-list">
      <li><svg class="tick"><use href="#tick"/></svg>Terassenbau</li>
      <li><svg class="tick"><use href="#tick"/></svg>Plasterarbeiten</li>
    </ul>
  </section>
</main>
</body>
</html>
```